MORVA Design

We have a 5 part framework that companies use to plot their social media strategies and digital transformation activity. We would like to display the 5 elements in a circular format (please see the attachment for our current design - we want to get a better version of that).

The five elements and their meaning can be read about here: http://quellagrove.example/morva/what-is-morva/
We would like to see designs that fit our corporate image but also maintain informality and simplicity…. Ive included another image of some of the icons we've been using and enjoying to give an understanding of the stuff we like

Target Market(s)

Corporates

Industry/Entity Type

Digital

Logo Text

Brokerage, Integration, Trust, Incentives, Leadership

Colors
0255a3

Requirements
Must have
• Must be circular in format with each element neatly labelled - PLEASE REVIEW OUR CURRENT VERSION IN THE ATTACHMENTS

```html
<!DOCTYPE html>
<html lang="en">
<head>
<meta charset="utf-8">
<title>MORVA Framework – Community Management</title>
<link rel="stylesheet" href="https://fonts.googleapis.com/css2?family=Roboto:wght@700&family=Roboto+Condensed:wght@700&display=swap">
<style>
  :root {
    --navy: #1e2a5a;
    --tint: #c9cde0;
    --paper: #ffffff;
    --haze: #eceef2;
  }
  html, body {
    margin: 0;
    padding: 0;
    width: 1200px;
    height: 900px;
    overflow: hidden;
  }
  .canvas {
    width: 1200px;
    height: 900px;
    background: radial-gradient(ellipse at 50% 50%, var(--paper) 55%, var(--haze) 100%);
  }
  .framework { display: block; }
  .ring-outer { fill: none; stroke: var(--navy); stroke-width: 8; stroke-dasharray: 120 6 40 6 80 6 140 6 60 6 90 6; }
  .ring-thin { fill: none; stroke: var(--navy); stroke-width: 2; }
  .ring-face { fill: var(--paper); stroke: var(--navy); stroke-width: 3; }
  .icon-slot { fill: var(--tint); }
  .connector { fill: var(--navy); }
  .element-label {
    font-family: "Roboto", Arial, sans-serif;
    font-weight: 700;
    font-size: 31px;
    letter-spacing: 1px;
    fill: var(--navy);
  }
  .hub-label {
    font-family: "Roboto Condensed", "Arial Narrow", sans-serif;
    font-weight: 700;
    font-size: 25px;
    fill: var(--navy);
    text-anchor: middle;
  }
</style>
</head>
<body>
<div class="canvas">
  <svg class="framework" width="1200" height="900" viewBox="0 0 1200 900" aria-label="MORVA framework: five elements around Community Management">
    <defs>
      <path id="arc-from-left" d="M -108 0 A 108 108 0 1 1 108 0 A 108 108 0 1 1 -108 0"/>
      <path id="arc-from-right" d="M 108 0 A 108 108 0 1 1 -108 0 A 108 108 0 1 1 108 0"/>
      <path id="arc-from-bottom" d="M 0 108 A 108 108 0 1 1 0 -108 A 108 108 0 1 1 0 108"/>
    </defs>

    <g class="connectors">
      <rect class="connector" x="-12" y="-4" width="24" height="8" transform="translate(675.4 350.7) rotate(36)"/>
      <rect class="connector" x="-12" y="-4" width="24" height="8" transform="translate(731.2 522.5) rotate(108)"/>
      <rect class="connector" x="-12" y="-4" width="24" height="8" transform="translate(585 628.7)"/>
      <rect class="connector" x="-12" y="-4" width="24" height="8" transform="translate(438.8 522.5) rotate(72)"/>
      <rect class="connector" x="-12" y="-4" width="24" height="8" transform="translate(494.7 350.7) rotate(-36)"/>
    </g>

    <g class="element element-brokerage" transform="translate(585 285)">
      <circle class="ring-outer" r="96" transform="rotate(20)"/>
      <circle class="ring-thin" r="88"/>
      <circle class="ring-face" r="83"/>
      <rect class="icon-slot" x="-46" y="-52" width="92" height="104" rx="8" role="img" aria-label="Icon: two tin-can telephones joined by a string"/>
      <text class="element-label"><textPath href="#arc-from-left" startOffset="25%" text-anchor="middle">BROKERAGE</textPath></text>
    </g>

    <g class="element element-integration" transform="translate(765.7 416.3)">
      <circle class="ring-outer" r="96" transform="rotate(110)"/>
      <circle class="ring-thin" r="88"/>
      <circle class="ring-face" r="83"/>
      <rect class="icon-slot" x="-42" y="-52" width="84" height="104" rx="8" role="img" aria-label="Icon: two building bricks with an arrow showing them snapping together"/>
      <text class="element-label"><textPath href="#arc-from-left" startOffset="47%" text-anchor="middle">INTEGRATION</textPath></text>
    </g>

    <g class="element element-trust" transform="translate(696.7 628.7)">
      <circle class="ring-outer" r="96" transform="rotate(200)"/>
      <circle class="ring-thin" r="88"/>
      <circle class="ring-face" r="83"/>
      <rect class="icon-slot" x="-68" y="-36" width="136" height="72" rx="8" role="img" aria-label="Icon: handshake between two suited arms"/>
      <text class="element-label"><textPath href="#arc-from-left" startOffset="61%" text-anchor="middle">BUILDING TRUST</textPath></text>
    </g>

    <g class="element element-incentives" transform="translate(473.3 628.7)">
      <circle class="ring-outer" r="96" transform="rotate(290)"/>
      <circle class="ring-thin" r="88"/>
      <circle class="ring-face" r="83"/>
      <rect class="icon-slot" x="-40" y="-48" width="80" height="96" rx="8" role="img" aria-label="Icon: wrapped gift box with a bow"/>
      <text class="element-label"><textPath href="#arc-from-right" startOffset="37.5%" text-anchor="middle">INCENTIVES</textPath></text>
    </g>

    <g class="element element-leadership" transform="translate(404.3 416.3)">
      <circle class="ring-outer" r="96" transform="rotate(60)"/>
      <circle class="ring-thin" r="88"/>
      <circle class="ring-face" r="83"/>
      <rect class="icon-slot" x="-56" y="-34" width="112" height="68" rx="8" role="img" aria-label="Icon: coach's whistle"/>
      <text class="element-label"><textPath href="#arc-from-bottom" startOffset="35%" text-anchor="middle">LEADERSHIP</textPath></text>
    </g>

    <g class="hub">
      <text class="hub-label" x="590" y="468">COMMUNITY</text>
      <text class="hub-label" x="590" y="502">MANAGEMENT</text>
    </g>
  </svg>
</div>
</body>
</html>
```